2024 Talon 2600 Remodeler Truck wrap.

We are a siding/window/roofing/painting company. see our website here: www.marlowsbridge-example.com.
I'd like a simple, bold, noticeable wrap with our logos and company colors.
Colors should stay simple: Dark Blue, White, Black, Gray.
Marlow's Bridge Construction was founded in Brindlewood County, Virginia in 2002 with the goal of providing the highest quality workmanship, and constantly striving to exceed our customer's expectations. Our company performs an array of both residential and commercial building services including roof and siding replacement, installation of new windows, or protecting your home with interior and exterior painting. ​

We are the ONLY home improvement company in Richmond, VA that can offer carpentry, painting, siding and windows. And we completely inspect your home for rotten wood and replace it (if needed) before we do anything else.

Target Market(s)

40-70 year old homeowners

Industry/Entity Type

Construction - remodeling

Colors

Designer to choose colors to be used in the design.

Requirements
Must have
• bold colors and large logos
Should not have
• bright red, bright yellow, people or tools

```html
<!DOCTYPE html>
<html lang="en">
<head>
<meta charset="utf-8">
<title>Marlow's Bridge Construction – Truck Wrap Side Panel</title>
<link rel="stylesheet" href="https://fonts.googleapis.com/css2?family=Exo+2:wght@400;600&display=swap">
<style>
  :root {
    --page-bg: #ffffff;
    --wrap-black: #1d1b1c;
    --wrap-navy: #1b2a4a;
    --stripe-white: #f4f5f7;
    --logo-silver: #d3d6da;
    --text-white: #ffffff;
    --text-gray: #b9bcc1;
  }
  html, body {
    margin: 0;
    width: 1200px;
    height: 1200px;
    overflow: hidden;
    background: var(--page-bg);
  }
  .wrap-panel {
    position: relative;
    width: 1200px;
    height: 1200px;
    font-family: "Exo 2", sans-serif;
  }
  .wrap-shapes {
    position: absolute;
    inset: 0;
  }
  .brand-square {
    position: absolute;
    left: 150px;
    top: 600px;
    width: 92px;
    height: 92px;
    background: var(--logo-silver);
  }
  .brand-name {
    position: absolute;
    left: 270px;
    top: 578px;
    margin: 0;
    font-weight: 600;
    font-size: 62px;
    line-height: 62px;
    letter-spacing: 1px;
    color: var(--logo-silver);
    text-transform: uppercase;
  }
  .service-list {
    position: absolute;
    left: 274px;
    top: 712px;
    margin: 0;
    font-weight: 400;
    font-size: 16px;
    letter-spacing: 1.5px;
    color: var(--text-gray);
    text-transform: uppercase;
  }
  .phone-number {
    position: absolute;
    right: 90px;
    top: 478px;
    margin: 0;
    font-weight: 600;
    font-size: 38px;
    letter-spacing: 3px;
    color: var(--text-white);
  }
  .web-address {
    position: absolute;
    right: 90px;
    top: 548px;
    margin: 0;
    font-weight: 400;
    font-size: 18px;
    letter-spacing: 1px;
    color: var(--text-white);
    text-transform: uppercase;
  }
</style>
</head>
<body>
  <main class="wrap-panel">
    <svg class="wrap-shapes" width="1200" height="1200" viewBox="0 0 1200 1200" aria-hidden="true">
      <polygon class="panel-body" points="70,770 70,600 150,470 1130,470 1130,770" fill="var(--wrap-black)"/>
      <polygon class="accent-band" points="150,470 1130,470 1130,528 114,528" fill="var(--wrap-navy)"/>
      <polygon class="accent-stripe" points="114,528 1130,528 1130,536 109,536" fill="var(--stripe-white)"/>
      <polygon class="band-tail" points="109,536 114,528 70,600 70,612" fill="var(--wrap-navy)"/>
    </svg>

    <div class="brand-square"></div>
    <h1 class="brand-name">Marlow's<br>Bridge</h1>
    <p class="service-list">Siding | Roofing | Windows | Painting</p>

    <p class="phone-number">555-210-4477</p>
    <p class="web-address">www.marlowsbridge-example.com</p>
  </main>
</body>
</html>
```